QTL Newsletter

QTL provides mortgage processing outsource services to Mortgage Lenders in Australia and New Zealand. The company employs approximately 300 staff based in offices in Sydney, Melbourne, Brisbane, Adelaide and Perth in Australia and Auckland, New Zealand.
The company acquired a similar and much larger business in 2012 which is being integrated into the one business.
The objectives of a newsletter are to:
- Support the development of the company culture
- Develp a sense of "one team"
- Provide a communication forum for management and staff
I am seeking design options for the newsletter. We will develop/include specific content which will likley evolve over time.
A copy of the company brand gudelines and logo is attached for reference. Our website is currently going through a redesign. Additional information can be provided on request.

Target Market(s)

The target market for the newsletter is staff. This is a diverse group in terms of locations, age, gender, occupations etc.

Industry/Entity Type

Communication

Requirements
Must have
• Information to be included in the newsletter should include:
- Business results (activity, volumes, performance to budget)
- Client news section (recent developments, client profiling etc)
- New initiatives (update on key projects and new business initiatives, initiatives roadmap)
- Office news (news section for each office including new employees, team profile of the month, report on social events)
- CEO report

```html
<!DOCTYPE html>
<html lang="en">
<head>
<meta charset="utf-8">
<title>QTL Newsletter — February 2013</title>
<link rel="stylesheet" href="https://fonts.googleapis.com/css2?family=Open+Sans:wght@300;400;600;700&display=swap">
<style>
:root{
  --brand-blue:#0d4a8b;
  --deep-blue:#0a3f78;
  --link-blue:#1b5ea8;
  --bright-blue:#1d7fd6;
  --olive:#9eab0c;
  --olive-dark:#8a9608;
  --white:#ffffff;
  --ink:#222222;
  --muted:#666666;
  --rule:rgba(255,255,255,.18);
}
*{margin:0;padding:0;box-sizing:border-box}
html,body{width:1200px;height:3799px;overflow:hidden}
body{font-family:"Open Sans",Arial,sans-serif;background:var(--white);position:relative;color:var(--white)}
.abs{position:absolute}

/* Masthead */
.masthead{left:0;top:0;width:1200px;height:260px;background:var(--white)}
.brand-name{left:88px;top:70px;font-size:104px;font-weight:600;color:var(--brand-blue);letter-spacing:2px;line-height:1}
.issue-date{left:830px;top:125px;display:flex;align-items:center;gap:22px;color:#333;font-size:30px;letter-spacing:1px}
.hero{left:0;top:260px;width:1200px;height:373px;background:linear-gradient(120deg,#e9eef5 0%,#a9bdd6 40%,#3f6fa3 75%,#143e70 100%)}
.social-strip{left:886px;top:538px;width:314px;height:95px;background:var(--olive);display:flex;align-items:center;justify-content:center;gap:18px}
.social-strip span{width:58px;height:58px;border:3px solid var(--white);border-radius:50%}
.strapline{left:0;top:633px;width:1200px;height:127px;background:var(--white);padding:28px 0 0 82px;color:#333}
.strapline h1{font-size:33px;font-weight:400;letter-spacing:.5px;line-height:1.2}
.strapline p{font-size:27px;line-height:1.3}

/* Main blue body */
.body-blue{left:0;top:760px;width:1200px;height:2944px;background:var(--brand-blue)}
.section-title{font-weight:400;font-size:32px;letter-spacing:.5px;text-transform:uppercase;border-bottom:2px solid var(--rule);padding-bottom:12px}
.lead{font-size:21px;font-weight:700;line-height:33px}
.big-title{font-size:50px;font-weight:400;letter-spacing:.3px;border-bottom:2px solid var(--rule);padding-bottom:14px}

.culture-title{left:82px;top:840px;width:1036px}
.culture-text{left:89px;top:945px;width:1030px}
.activity-title{left:82px;top:1198px;width:1036px}
.activity-text{left:89px;top:1325px;width:700px}
.activity-photo{left:798px;top:1317px;width:316px;height:203px;border:4px solid #2d6bab;background:linear-gradient(135deg,#f2f2f2,#c9ced6 55%,#7ea3c8)}

.client-title{left:82px;top:1602px;width:1036px}
.card{top:1694px;width:498px;height:462px;background:var(--white);padding:36px 34px;color:var(--ink)}
.card h3{font-size:32px;font-weight:400;color:var(--link-blue);line-height:1.2}
.card time{display:block;font-size:20px;color:var(--olive);margin:6px 0 20px}
.card p{font-size:19px;line-height:31px;color:#333}
.btn{display:inline-block;font-size:18px;font-weight:600;color:var(--white);padding:14px 16px;border-radius:6px;text-transform:uppercase}
.btn-olive{background:var(--olive);position:absolute;left:34px;bottom:38px}
.btn-blue{background:var(--bright-blue)}
.card-left{left:82px}
.card-right{left:624px}

.results-title{left:82px;top:2222px;width:1036px}
.results-photo{left:174px;top:2349px;width:231px;height:209px;border:4px solid #2d6bab;background:linear-gradient(160deg,#dfe4e8,#6f8899 45%,#2e4a5c 70%,#7fa35a)}
.results-copy{left:443px;top:2343px;width:682px}
.results-copy .btn{margin-top:18px}

/* New initiatives */
.initiatives{left:0;top:2637px;width:1200px;height:503px;background:var(--white)}
.initiatives-tab{left:0;top:2637px;width:200px;height:503px}
.initiatives-label{left:-110px;top:2855px;width:420px;text-align:center;font-size:48px;font-weight:300;transform:rotate(-90deg);color:var(--white)}
.initiative{left:247px;width:900px;display:flex;gap:34px;color:var(--ink)}
.initiative .thumb{width:298px;height:175px;flex:none;border:3px solid #d0d6dc;background:linear-gradient(160deg,#e2e7eb,#70899a 45%,#2e4a5c 72%,#86a85e)}
.initiative h4{font-size:21px;font-weight:400;color:var(--link-blue)}
.initiative .sub{font-size:21px;color:var(--olive)}
.initiative p{font-size:21px;line-height:31px;color:#333}
.item-one{top:2690px}
.item-two{top:2910px}

/* CEO report */
.ceo-band{left:0;top:3198px;width:1200px;height:285px;background:var(--olive)}
.ceo-photo{left:38px;top:3150px;width:294px;height:350px;border:12px solid var(--white);background:var(--brand-blue)}
.ceo-title{left:450px;top:3222px;font-size:44px;font-weight:300}
.ceo-text{left:450px;top:3290px;width:700px;font-size:19px;font-weight:700;line-height:31px}

/* Footer */
.footer-social{left:0;top:3595px;width:1200px;display:flex;justify-content:center;gap:12px}
.footer-social span{width:64px;height:64px;border-radius:50%;background:var(--olive)}
.legal{left:0;top:3715px;width:1200px;text-align:center;font-size:21px;line-height:30px;color:var(--muted)}
</style>
</head>
<body>

<header class="abs masthead">
  <div class="abs brand-name">QTL</div>
  <div class="abs issue-date">
    <svg width="62" height="66" viewBox="0 0 62 66" aria-hidden="true">
      <circle cx="31" cy="37" r="24" fill="none" stroke="#8fa400" stroke-width="6"/>
      <rect x="25" y="2" width="12" height="7" rx="2" fill="#8fa400"/>
      <rect x="28" y="8" width="6" height="6" fill="#8fa400"/>
      <path d="M31 37 L31 23 M31 37 L41 43" stroke="#8fa400" stroke-width="4" stroke-linecap="round"/>
    </svg>
    <span>FEBRUARY 2013</span>
  </div>
</header>

<div class="abs hero" role="img" aria-label="Photo of a mortgage contract document with a set of house keys"></div>
<div class="abs social-strip" aria-label="Social links"><span></span><span></span><span></span></div>

<section class="abs strapline">
  <h1>PROVIDES MORTGAGE PROCESSING OUTSOURCE SERVICES</h1>
  <p>to Mortgage Lenders in Australia and New Zealand</p>
</section>

<main class="abs body-blue"></main>

<h2 class="abs section-title culture-title">Company Culture</h2>
<p class="abs lead culture-text">Lorem Ipsum is simply dummy text of the printing and typesetting industry. Lorem Ipsum has been the industry's standard dummy text ever since the 1500s, when an unknown printer took a galley of type and scrambled it to make a type specimen book. It has survived not only five centuries, but also the leap into electronic typesetting, remaining essentially unchanged.</p>

<h2 class="abs section-title activity-title">Business Activity</h2>
<p class="abs lead activity-text">Lorem Ipsum is simply dummy text of the printing and typesetting industry. Lorem Ipsum has been the industry's standard dummy text ever since the 1500s, when an unknown printer took a galley of type and scrambled it to make a type specimen book. It has survived not only five centuries, but also the leap into electronic typesetting, remaining essentially unchanged.</p>
<div class="abs activity-photo" role="img" aria-label="Photo of mortgage paperwork with a calculator and pen on a desk"></div>

<h2 class="abs big-title client-title">Client news</h2>
<article class="abs card card-left">
  <h3>Client news1</h3>
  <time>04.02.2013</time>
  <p>Lorem Ipsum is simply dummy text of the printing and typesetting industry. Lorem Ipsum has been the industry's standard dummy text ever since the 1500s, when an unknown printer took a galley of type and scrambled it to make a type specimen book</p>
  <a class="btn btn-olive">Read more</a>
</article>
<article class="abs card card-right">
  <h3>Client news1</h3>
  <time>04.02.2013</time>
  <p>Lorem Ipsum is simply dummy text of the printing and typesetting industry. Lorem Ipsum has been the industry's standard dummy text ever since the 1500s, when an unknown printer took a galley of type and scrambled it to make a type specimen book</p>
  <a class="btn btn-olive">Read more</a>
</article>

<h2 class="abs big-title results-title">Business results</h2>
<div class="abs results-photo" role="img" aria-label="Photo of a monitor showing financial market charts"></div>
<div class="abs results-copy">
  <p class="lead">Lorem Ipsum is simply dummy text of the printing and typesetting industry. Lorem Ipsum has been the industry's standard dummy text ever since the 1500s, when an unknown printer took a galley of type and scrambled it to make a type specimen book.</p>
  <a class="btn btn-blue">Read more</a>
</div>

<section class="abs initiatives"></section>
<svg class="abs initiatives-tab" viewBox="0 0 200 503" aria-hidden="true">
  <polygon points="0,0 165,0 165,215 198,251 165,287 165,503 0,503" fill="#9eab0c"/>
</svg>
<h2 class="abs initiatives-label">New initiatives</h2>
<article class="abs initiative item-one">
  <div class="thumb" role="img" aria-label="Photo of a monitor showing financial market charts"></div>
  <div>
    <h4>Heading Main</h4>
    <div class="sub">Subheading</div>
    <p>Lorem Ipsum is simply dummy text of the printing and typesetting industry. Lorem Ipsum has been the industry's standard dummy text ever since the 1500s,</p>
  </div>
</article>
<article class="abs initiative item-two">
  <div class="thumb" role="img" aria-label="Photo of a monitor showing financial market charts"></div>
  <div>
    <h4>Heading Main</h4>
    <div class="sub">Subheading</div>
    <p>Lorem Ipsum is simply dummy text of the printing and typesetting industry. Lorem Ipsum has been the industry's standard dummy text ever since the 1500s,</p>
  </div>
</article>

<section class="abs ceo-band"></section>
<div class="abs ceo-photo" role="img" aria-label="Portrait of the CEO"></div>
<h2 class="abs ceo-title">CEO report</h2>
<p class="abs ceo-text">Lorem Ipsum is simply dummy text of the printing and typesetting industry. Lorem Ipsum has been the industry's standard dummy text ever since the 1500s, when an unknown printer took a galley of type and scrambled it to make a type specimen book</p>

<div class="abs footer-social" aria-label="Social links"><span></span><span></span><span></span></div>
<footer class="abs legal">
  <p>You are receiving this email as a part of your company's program.</p>
  <p>Copyright © 2012 QTL All rights reserved.</p>
</footer>

</body>
</html>
```